Im open to ideas.. I was thinking on my business cards aswell as my logo. a place for my name. email. phone number and abn..

ive attched a file with my business logo. which i dont love the colours.. i was think a dark background with charcoal letters so something along those colour schumes but im open to ideas..

Business

BRL Constructions

```html
<!DOCTYPE html>
<html lang="en">
<head>
<meta charset="utf-8">
<title>BRL Constructions – Business Card</title>
<link rel="stylesheet" href="https://fonts.googleapis.com/css2?family=Montserrat:wght@400;600&display=swap">
<style>
  :root {
    --page-bg: #ffffff;
    --card-dark: #000000;
    --card-light: #ffffff;
    --ink: #111111;
    --ink-inverse: #ffffff;
    --edge: #c9c9c9;
    --divider: #222222;
  }
  html, body {
    margin: 0;
    padding: 0;
    width: 1200px;
    height: 1000px;
    overflow: hidden;
    background: var(--page-bg);
    font-family: "Montserrat", Arial, sans-serif;
  }
  .business-card {
    position: absolute;
    left: 316px;
    top: 337px;
    width: 568px;
    height: 326px;
    background: var(--card-light);
  }
  .brand-band {
    position: absolute;
    left: 0;
    top: 0;
    width: 100%;
    height: 196px;
    background: var(--card-dark);
    display: flex;
    align-items: center;
    justify-content: center;
  }
  .brand-name {
    margin: 40px 0 0;
    color: var(--ink-inverse);
    font-weight: 600;
    font-size: 40px;
    letter-spacing: 2px;
    text-transform: uppercase;
  }
  .contact-band {
    position: absolute;
    left: 0;
    top: 196px;
    width: 100%;
    height: 90px;
    box-sizing: border-box;
    border-left: 1px solid var(--edge);
    border-right: 1px solid var(--edge);
    color: var(--ink);
    font-size: 16px;
    line-height: 20.5px;
  }
  .contact-person {
    position: absolute;
    left: 68px;
    top: 8px;
  }
  .contact-divider {
    position: absolute;
    left: 314px;
    top: 11px;
    width: 1px;
    height: 68px;
    background: var(--divider);
  }
  .contact-lines {
    position: absolute;
    left: 364px;
    top: 8px;
  }
  .contact-band p { margin: 0; }
  .abn-band {
    position: absolute;
    left: 0;
    bottom: 0;
    width: 100%;
    height: 40px;
    background: var(--card-dark);
    color: var(--ink-inverse);
    font-size: 14px;
    display: flex;
    align-items: center;
    justify-content: center;
    letter-spacing: 0.3px;
  }
</style>
</head>
<body>
  <article class="business-card">
    <header class="brand-band">
      <h1 class="brand-name">BRL Constructions</h1>
    </header>
    <section class="contact-band">
      <div class="contact-person">
        <p class="person-name">Name</p>
        <p class="person-title">Title</p>
        <p class="person-address">Add: 123 address here</p>
      </div>
      <div class="contact-divider"></div>
      <div class="contact-lines">
        <p class="contact-phone">P: 123 4567</p>
        <p class="contact-email">E: 123@456.com</p>
      </div>
    </section>
    <footer class="abn-band">ABN: 123456789</footer>
  </article>
</body>
</html>
```